GlowRA (Beer/Wine candles) Edgy Candle with a Cause

Help us to help others. GlowRa is a beautifully scented natural soy candle made using repurposed beer/ wine bottles while at the same time donating a portion of our profits to youth alcohol education programs. (1. Waste = Repurposed beer/wine bottle, 2.) GlowRa = (anti) drunk/alcohol 3.) Ed = education/prevention programs.)
We're looking for a design that is cool and bold yet elegant and appeals to women (90% of our customers.) No traditional beer label designs please.

The "GlowRA" logo should appear prominently in the design with the scent name (in a different font) "on top." (See the "Chocolate Glowra" poster attached.

Examples of actual scents: Amber Drift, Velvet Sunrise, Frosted Mintleaf. (None of the fragrances smell like beer/alcohol or wine.)

Also the ED in GlowRRA should stand out in some way.

The emphasis should not be on the recycling aspect, so no obvious recycling symbols.

We are open to different interpretations and have attached varying examples that we like.
Note: a "blackboard/chalkboard" label is an idea since this deals with education.

Note: files & fonts used in the final design should be editable so that we can add other scent names as needed.

Target Market(s)

Candle buyers, specifically women between the ages of 16-45

Requirements
Must have
• 1.)Free fonts or license fonts under $20.00 2.) fonts modified to look unique/original. 3.) Editable Scent name 4.) Burning instructions 5.) Warning Info
• Burning Instructions: Trim wick to 1/4" before each lighting. Keep free from foreign materials including wick trimmings. For an even burn, burn for at least 1 hour but not more than 4 hours at a time. Discontinue use when 1/4" of wax remains. Discard or recycle after use.
• Warning: Burn candle within sight. Keep out of reach of children and pets. Keep away from things that catch fire. Use with caution.
Nice to have
• Colored Scent Names
Should not have
• recycle symbols

```html
<!DOCTYPE html>
<html lang="en">
<head>
<meta charset="utf-8">
<title>GlowRA Amber Drift Soy Candle Label</title>
<link href="https://fonts.googleapis.com/css2?family=Exo+2:wght@200;300&family=Russo+One&family=Great+Vibes&family=Gochi+Hand&display=swap" rel="stylesheet">
<style>
  :root {
    --page: #ffffff;
    --chalkboard: #353638;
    --chalk: #ececec;
    --amber: #c8862f;
    --bark: #7a4524;
    --stop-red: #d42a2a;
  }
  html, body {
    margin: 0;
    padding: 0;
    width: 1200px;
    height: 817px;
    overflow: hidden;
    background: var(--page);
  }
  .canvas {
    position: relative;
    width: 1200px;
    height: 817px;
  }
  .label {
    position: absolute;
    left: 103px;
    top: 103px;
    width: 994px;
    height: 611px;
    background: var(--chalkboard);
    overflow: hidden;
  }
  .label-frame {
    position: absolute;
    left: 0;
    top: 0;
    width: 994px;
    height: 611px;
  }
  .side-copy {
    position: absolute;
    font-family: "Exo 2", sans-serif;
    font-weight: 200;
    color: var(--chalk);
    font-size: 22px;
    line-height: 29.5px;
    transform: rotate(-90deg);
    transform-origin: top left;
    margin: 0;
  }
  .side-copy .lead { color: var(--chalk); }
  .side-copy .body { color: var(--amber); }
  .burning-instructions {
    left: 38px;
    top: 585px;
    width: 560px;
  }
  .burning-instructions .body { color: var(--chalk); }
  .burning-instructions .lead { color: var(--chalk); }
  .burning-instructions .highlight { color: var(--amber); }
  .warning {
    left: 849px;
    top: 470px;
    width: 430px;
  }
  .scent-name {
    position: absolute;
    left: 230px;
    top: 70px;
    width: 640px;
    text-align: center;
    font-family: "Great Vibes", cursive;
    font-size: 72px;
    line-height: 1;
    color: var(--amber);
    margin: 0;
    text-shadow: 0 0 0 var(--bark), 3px 3px 0 var(--bark), -3px -3px 0 var(--bark), 3px -3px 0 var(--bark), -3px 3px 0 var(--bark);
  }
  .brand-name {
    position: absolute;
    left: 237px;
    top: 150px;
    width: 600px;
    text-align: center;
    font-family: "Russo One", sans-serif;
    font-size: 138px;
    line-height: 1;
    color: var(--chalk);
    margin: 0;
    letter-spacing: 2px;
  }
  .product-type {
    position: absolute;
    left: 287px;
    top: 315px;
    width: 500px;
    text-align: center;
    font-family: "Gochi Hand", cursive;
    font-size: 62px;
    line-height: 1;
    color: var(--amber);
    margin: 0;
  }
  .spec {
    position: absolute;
    font-family: "Russo One", sans-serif;
    font-size: 31px;
    line-height: 36px;
    margin: 0;
  }
  .spec-burn-time {
    left: 278px;
    top: 382px;
    color: var(--chalk);
    transform: rotate(5deg);
  }
  .spec-weight {
    left: 520px;
    top: 396px;
    width: 80px;
    text-align: center;
    color: var(--amber);
  }
  .spec-hand-poured {
    left: 700px;
    top: 380px;
    text-align: right;
    color: var(--chalk);
    transform: rotate(-8deg);
  }
  .cause {
    position: absolute;
    left: 367px;
    top: 508px;
    width: 440px;
    text-align: center;
    font-family: "Gochi Hand", cursive;
    font-size: 31px;
    line-height: 40px;
    color: var(--amber);
    margin: 0;
    transform: rotate(1deg);
  }
  .age-restriction {
    position: absolute;
    left: 857px;
    top: 485px;
    width: 100px;
    height: 100px;
  }
</style>
</head>
<body>
<main class="canvas">
  <section class="label">
    <svg class="label-frame" viewBox="0 0 994 611" aria-hidden="true">
      <path d="M14 20 Q250 12 497 18 T980 16 Q986 150 982 305 T984 596 Q740 590 497 595 T12 592 Q18 450 14 305 T14 20 Z"
            fill="none" stroke="var(--bark)" stroke-width="5" stroke-linejoin="round"/>
    </svg>

    <p class="side-copy burning-instructions">
      <span class="lead">Burning Instructions: </span><span class="highlight">Trim wick to 1/4" before each lighting. Keep free from foreign materials including wick trimmings. For an even burn, burn for at least 1 hour but not more than 4 hours at a time. Discontinue use when 1/4" of wax remains. Discard or recycle after use.</span>
    </p>

    <h2 class="scent-name">Amber Drift</h2>
    <h1 class="brand-name">GlowRA</h1>
    <p class="product-type">Soy Candle</p>

    <p class="spec spec-burn-time">48HR<br>BURN TIME</p>
    <p class="spec spec-weight">100 G</p>
    <p class="spec spec-hand-poured">HAND-<br>POURED</p>

    <p class="cause">Donating a portion of profits to youth alcohol education programs</p>

    <p class="side-copy warning">
      <span class="lead">Warning: </span><span class="body">Burn candle within sight. Keep out of reach of children and pets. Keep away from things that catch fire. Use with caution.</span>
    </p>

    <svg class="age-restriction" viewBox="0 0 100 100" role="img" aria-label="Not for under 18 notice">
      <circle cx="50" cy="50" r="43" fill="none" stroke="var(--stop-red)" stroke-width="7"/>
      <line x1="80" y1="20" x2="20" y2="80" stroke="var(--stop-red)" stroke-width="7"/>
    </svg>
  </section>
</main>
</body>
</html>
```